Mobile technology Business Card Design Project

We need a business card design for our company based in Sydeny Australia, that takes a company's desktop sites and creates a mobile site compatible to all mobile/smartphone devices. This allows greater ease of use and generally faster business conversion than customers using a desktop site.
Our company is called VelqCore but we refer to it as Velq Corestreams. If this could be represented somewhere on the business card that would be great.
Am open to suggestions regarding the colours but a high tech  theme would be good.
Happy bidding!

Target Market(s)
Business owner that has a website and is reasonably savvy regarding online/mobile marketing.
Industry/Entity Type
Business
Requirements
Must have
- Business card details:
Director Peter Langwade
Address: 5/41 Dunmore rd, Kelbrook. 2087
Email: tbc
Web: www.velqcore.com.au
The cards need to have two different names for the two directors.
Gregory Halvane & Peter Langwade (two separate business cards)

```html
<!DOCTYPE html>
<html lang="en">
<head>
<meta charset="utf-8">
<title>VelqCore Business Card</title>
<link rel="stylesheet" href="https://fonts.googleapis.com/css2?family=Montserrat:wght@500;600;700&display=swap">
<style>
  :root {
    --stage: #2b2b2b;
    --orange: #ef8a06;
    --orange-light: #f7a21c;
    --orange-deep: #e57a00;
    --blue: #1b8fc9;
    --ink: #1c1c1c;
    --paper: #ffffff;
    --paper-shade: #e9e9e9;
    --white: #ffffff;
  }
  * { margin: 0; padding: 0; box-sizing: border-box; }
  html, body {
    width: 1200px;
    height: 900px;
    overflow: hidden;
    background: var(--stage);
    font-family: "Montserrat", sans-serif;
  }
  .sheet {
    position: relative;
    width: 1200px;
    height: 900px;
  }
  .card {
    position: absolute;
    left: 250px;
    width: 700px;
    height: 400px;
    border-radius: 28px;
    overflow: hidden;
  }
  /* Front side */
  .card--front {
    top: 30px;
    background: radial-gradient(circle at 30% 70%, var(--orange-light) 0%, var(--orange) 45%, var(--orange-deep) 100%);
  }
  .card--front .brand {
    position: absolute;
    left: 200px;
    top: 150px;
    display: flex;
    align-items: center;
    gap: 26px;
  }
  .card--front .brand-dot {
    width: 96px;
    height: 96px;
    border-radius: 50%;
    background: var(--white);
    flex: none;
  }
  .card--front .brand-name {
    font-size: 50px;
    font-weight: 600;
    color: var(--white);
    letter-spacing: 1px;
    line-height: 1;
  }
  .card--front .tagline {
    margin-top: 8px;
    font-size: 17px;
    font-weight: 600;
    color: var(--white);
    letter-spacing: 1.2px;
  }
  /* Back side */
  .card--back {
    top: 470px;
    background: radial-gradient(circle at 25% 40%, var(--paper) 0%, var(--paper) 40%, var(--paper-shade) 100%);
  }
  .card--back .brand {
    position: absolute;
    left: 46px;
    top: 56px;
    width: 290px;
    display: flex;
    flex-direction: column;
    align-items: center;
  }
  .card--back .brand-dot {
    width: 170px;
    height: 170px;
    border-radius: 50%;
    background: var(--orange);
  }
  .card--back .brand-name {
    margin-top: 26px;
    font-size: 52px;
    font-weight: 600;
    color: var(--ink);
    letter-spacing: 1px;
    line-height: 1;
  }
  .card--back .tagline {
    margin-top: 8px;
    font-size: 17px;
    font-weight: 600;
    color: var(--orange);
    letter-spacing: 1.2px;
  }
  .details {
    position: absolute;
    left: 392px;
    top: 78px;
    color: var(--ink);
  }
  .details .person-name {
    font-size: 20px;
    font-weight: 600;
    color: var(--orange);
    letter-spacing: 1px;
    text-transform: uppercase;
  }
  .details .person-role {
    margin-top: 6px;
    font-size: 13px;
    font-weight: 600;
  }
  .details .company {
    margin-top: 26px;
    font-size: 14px;
    font-weight: 700;
    color: var(--blue);
  }
  .details .address {
    margin-top: 4px;
    font-size: 14px;
    font-weight: 500;
  }
  .contact {
    margin-top: 30px;
    display: grid;
    grid-template-columns: 58px auto;
    row-gap: 6px;
    font-size: 14px;
    font-weight: 500;
  }
  .contact dt { color: var(--blue); }
  .contact dd { color: var(--ink); }
</style>
</head>
<body>
<main class="sheet">
  <section class="card card--front" aria-label="Card front">
    <div class="brand">
      <span class="brand-dot"></span>
      <div>
        <div class="brand-name">VelqCore</div>
        <div class="tagline">Sites Built for Pockets</div>
      </div>
    </div>
  </section>

  <section class="card card--back" aria-label="Card back">
    <div class="brand">
      <span class="brand-dot"></span>
      <div class="brand-name">VelqCore</div>
      <div class="tagline">Sites Built for Pockets</div>
    </div>
    <div class="details">
      <div class="person-name">Peter Langwade</div>
      <div class="person-role">Director</div>
      <div class="company">Velq Corestreams</div>
      <div class="address">5/41 Dunmore rd, Kelbrook. 2087</div>
      <dl class="contact">
        <dt>Phone</dt><dd>9000 412 736</dd>
        <dt>Email</dt><dd>info@velqcore.com.au</dd>
        <dt>Web</dt><dd>www.velqcore.com.au</dd>
      </dl>
    </div>
  </section>
</main>
</body>
</html>
```